Stationary for Logistics Co.
Brevin Haulage Group
Project: Stationary for Logistics Co.
Stationary for Logistics Co.  - Transportation
Creative Brief
Professional
Colin Dartley
Director of Sales
4215 Marlow Ln. Cincinnati, Ohio 45239
513.620.5174 Ext. 37
colindartley@brevinhaul.example
www.brevinhaul.example
brevinhaul brevinhaul
We need business card, letterhead and envelope design. Thanks

```html
<!DOCTYPE html>
<html lang="en">
<head>
<meta charset="utf-8">
<title>Brevin Haulage Group Stationery</title>
<link href="https://fonts.googleapis.com/css2?family=Roboto+Condensed:wght@400;700&family=Roboto:wght@400;500;700&display=swap" rel="stylesheet">
<style>
  :root {
    --navy: #1f2f6e;
    --red: #c4232f;
    --paper: #ffffff;
    --backdrop: #dcdde0;
    --ink: #2d2d33;
    --muted: #6b6f7a;
  }
  * { box-sizing: border-box; margin: 0; padding: 0; }
  html, body { width: 1200px; height: 790px; overflow: hidden; }
  body {
    background: var(--backdrop);
    font-family: "Roboto", Arial, sans-serif;
    color: var(--ink);
    position: relative;
  }
  .sheet {
    position: absolute;
    background: var(--paper);
    box-shadow: 0 6px 18px rgba(0,0,0,.18);
    overflow: hidden;
  }
  .brand { display: flex; align-items: center; gap: 8px; }
  .brand-dot { border-radius: 50%; background: var(--red); flex: none; }
  .brand-name {
    font-family: "Roboto Condensed", Arial, sans-serif;
    font-weight: 700;
    color: var(--navy);
    line-height: 1;
  }
  .brand-tag {
    font-family: "Roboto Condensed", Arial, sans-serif;
    color: var(--muted);
    letter-spacing: .04em;
    margin-top: 3px;
  }

  /* Letterhead */
  .letterhead { left: 40px; top: 35px; width: 509px; height: 720px; }
  .letterhead .brand { position: absolute; left: 48px; top: 44px; }
  .letterhead .brand-dot { width: 34px; height: 34px; }
  .letterhead .brand-name { font-size: 20px; }
  .letterhead .brand-tag { font-size: 9px; }
  .side-band { position: absolute; left: 0; top: 110px; bottom: 0; width: 26px; display: flex; }
  .side-band .red { width: 16px; background: var(--red); }
  .side-band .navy { width: 6px; background: var(--navy); margin-left: 4px; }
  .corner-band { position: absolute; left: 0; top: 0; width: 26px; height: 96px; display: flex; }
  .corner-band .red { width: 16px; background: var(--red); }
  .corner-band .navy { width: 6px; background: var(--navy); margin-left: 4px; }
  .bottom-band { position: absolute; left: 0; right: 0; bottom: 0; height: 16px; background: var(--red); }
  .bottom-band::before { content: ""; position: absolute; left: 0; right: 0; top: -10px; height: 6px; background: var(--navy); }
  .watermark {
    position: absolute; left: 50%; top: 44%; transform: translate(-50%,-50%);
    display: flex; flex-direction: column; align-items: center; gap: 12px; opacity: .12;
  }
  .watermark .brand-dot { width: 120px; height: 120px; }
  .watermark .brand-name { font-size: 22px; }
  .letter-address {
    position: absolute; left: 48px; bottom: 46px;
    display: flex; align-items: flex-start; gap: 8px;
    font-size: 11px; line-height: 1.45; color: var(--ink);
  }
  .letter-address svg { flex: none; margin-top: 2px; }

  /* Envelope */
  .envelope { left: 600px; top: 40px; width: 560px; height: 280px; }
  .env-band { position: absolute; left: 0; right: 0; top: 0; height: 18px; background: var(--red); }
  .env-band::after { content: ""; position: absolute; left: 0; right: 0; top: 22px; height: 5px; background: var(--navy); }
  .envelope .brand { position: absolute; left: 30px; top: 46px; }
  .envelope .brand-dot { width: 30px; height: 30px; }
  .envelope .brand-name { font-size: 17px; }
  .envelope .brand-tag { font-size: 8px; }
  .env-address { position: absolute; left: 70px; top: 92px; font-size: 9px; color: var(--muted); line-height: 1.4; }
  .env-foot { position: absolute; left: 0; right: 0; bottom: 0; height: 8px; background: var(--navy); }

  /* Business cards */
  .card { top: 380px; width: 270px; height: 154px; }
  .card-front { left: 600px; }
  .card-back { left: 890px; }
  .card-edge { position: absolute; left: 0; top: 0; bottom: 0; width: 16px; display: flex; }
  .card-edge .red { width: 9px; background: var(--red); }
  .card-edge .navy { width: 4px; background: var(--navy); margin-left: 3px; }
  .card-front .brand { position: absolute; left: 32px; top: 30px; }
  .card-front .brand-dot { width: 26px; height: 26px; }
  .card-front .brand-name { font-size: 14px; }
  .card-front .brand-tag { font-size: 7px; }
  .name-bar {
    position: absolute; left: 32px; right: 0; top: 84px; height: 40px;
    background: var(--navy); color: #fff; padding: 7px 12px;
  }
  .name-bar .person { font-family: "Roboto Condensed", Arial, sans-serif; font-weight: 700; font-size: 14px; }
  .name-bar .role { font-size: 9px; opacity: .85; margin-top: 2px; }
  .card-back .top-band { position: absolute; left: 0; right: 0; top: 0; height: 8px; background: var(--red); }
  .card-back .top-band::after { content: ""; position: absolute; left: 0; right: 0; top: 10px; height: 3px; background: var(--navy); }
  .card-back .brand { position: absolute; left: 20px; top: 28px; }
  .card-back .brand-dot { width: 20px; height: 20px; }
  .card-back .brand-name { font-size: 12px; }
  .contact-list { position: absolute; left: 20px; top: 62px; list-style: none; font-size: 9.5px; line-height: 1.6; }
  .contact-list li { display: flex; align-items: center; gap: 6px; }
  .contact-list svg { flex: none; }
</style>
</head>
<body>

<section class="sheet letterhead" aria-label="Letterhead">
  <div class="corner-band"><span class="red"></span><span class="navy"></span></div>
  <div class="side-band"><span class="red"></span><span class="navy"></span></div>
  <div class="brand">
    <span class="brand-dot"></span>
    <div>
      <div class="brand-name">Brevin Haulage Group</div>
      <div class="brand-tag">Freight &amp; Logistics Solutions</div>
    </div>
  </div>
  <div class="watermark" aria-hidden="true">
    <span class="brand-dot"></span>
    <span class="brand-name">Brevin Haulage Group</span>
  </div>
  <div class="letter-address">
    <svg width="10" height="14" viewBox="0 0 10 14"><path d="M5 0a5 5 0 0 0-5 5c0 3.6 5 9 5 9s5-5.4 5-9a5 5 0 0 0-5-5zm0 7a2 2 0 1 1 0-4 2 2 0 0 1 0 4z" fill="var(--navy)"/></svg>
    <p>4215 Marlow Ln.<br>Cincinnati, Ohio 45239</p>
  </div>
  <div class="bottom-band"></div>
</section>

<section class="sheet envelope" aria-label="Envelope">
  <div class="env-band"></div>
  <div class="brand">
    <span class="brand-dot"></span>
    <div>
      <div class="brand-name">Brevin Haulage Group</div>
      <div class="brand-tag">Freight &amp; Logistics Solutions</div>
    </div>
  </div>
  <p class="env-address">4215 Marlow Ln. Cincinnati, Ohio 45239</p>
  <div class="env-foot"></div>
</section>

<section class="sheet card card-front" aria-label="Business card front">
  <div class="card-edge"><span class="red"></span><span class="navy"></span></div>
  <div class="brand">
    <span class="brand-dot"></span>
    <div>
      <div class="brand-name">Brevin Haulage Group</div>
      <div class="brand-tag">Freight &amp; Logistics Solutions</div>
    </div>
  </div>
  <div class="name-bar">
    <div class="person">Colin Dartley</div>
    <div class="role">Director of Sales</div>
  </div>
</section>

<section class="sheet card card-back" aria-label="Business card back">
  <div class="top-band"></div>
  <div class="brand">
    <span class="brand-dot"></span>
    <div class="brand-name">Brevin Haulage Group</div>
  </div>
  <ul class="contact-list">
    <li><svg width="9" height="12" viewBox="0 0 10 14"><path d="M5 0a5 5 0 0 0-5 5c0 3.6 5 9 5 9s5-5.4 5-9a5 5 0 0 0-5-5zm0 7a2 2 0 1 1 0-4 2 2 0 0 1 0 4z" fill="var(--red)"/></svg>4215 Marlow Ln. Cincinnati, Ohio 45239</li>
    <li><svg width="10" height="10" viewBox="0 0 10 10"><path d="M2 0l2 2.5-1.2 1.3a6 6 0 0 0 3.4 3.4L7.5 6 10 8l-1.5 2C4 10 0 6 0 1.5z" fill="var(--red)"/></svg>513.620.5174 Ext. 37</li>
    <li><svg width="10" height="8" viewBox="0 0 10 8"><rect width="10" height="8" fill="var(--red)"/><path d="M0 0l5 4 5-4" stroke="#fff" fill="none"/></svg>colindartley@brevinhaul.example</li>
    <li><svg width="10" height="10" viewBox="0 0 10 10"><circle cx="5" cy="5" r="4.5" fill="none" stroke="var(--red)"/><path d="M0.5 5h9M5 0.5c-2.5 3-2.5 6 0 9M5 0.5c2.5 3 2.5 6 0 9" stroke="var(--red)" fill="none" stroke-width=".8"/></svg>www.brevinhaul.example</li>
  </ul>
</section>

</body>
</html>
```